Dorans Greens

We require an A4 landscape leaflet with a fold down the middle, designed on all 4 sides to represent our home delivery fruit and vegetable box scheme. The leaflet should emphasize on our Free Trial Box offer (no commitment/obligation / £2 delivery charge applies / contents are 100% free) Offer applies to our small box only. We do a large box for £18.50, a medium box for £13 and a small box for £7.50. The leaflet should also show that we deliver extra products such as milk, artisan bread, meat boxes, fresh fish boxes, award winning sausage/pies etc
For more info on our service visit www.doransgreens.co.uk
Updates

Project Deadline Extended
Reason: Currently away so need more time to decide and apply changes required.

Industry/Entity Type

Landscape

```html
<!DOCTYPE html>
<html lang="en">
<head>
<meta charset="utf-8">
<title>Dorans Greens – Leaflet</title>
<link href="https://fonts.googleapis.com/css2?family=Della+Respira&family=Kalam:wght@400;700&family=Sorts+Mill+Goudy&display=swap" rel="stylesheet">
<style>
  :root {
    --page: #ffffff;
    --wood-dark: #4a2a17;
    --wood-mid: #7a4a2c;
    --wood-light: #9a6441;
    --parchment: #ece5c8;
    --parchment-edge: #d8cda3;
    --ink: #2a2418;
    --cream: #ffffff;
    --red: #d42a1f;
    --green-rule: #7fb08a;
    --burst: #ffe61c;
    --burst-ink: #d6201a;
    --photo-border: #ffffff;
  }
  * { margin: 0; padding: 0; box-sizing: border-box; }
  html, body { width: 825px; height: 1200px; overflow: hidden; background: var(--page); }
  .canvas { position: relative; width: 825px; height: 1200px; overflow: hidden; }

  .panel { position: absolute; overflow: hidden; }
  .panel--wood {
    background:
      repeating-linear-gradient(90deg, rgba(0,0,0,.08) 0 2px, transparent 2px 38px),
      repeating-linear-gradient(90deg, rgba(255,255,255,.04) 0 1px, transparent 1px 13px),
      linear-gradient(180deg, var(--wood-mid), var(--wood-light) 45%, var(--wood-dark));
  }
  .panel--parchment {
    background: radial-gradient(ellipse at center, var(--parchment) 55%, var(--parchment-edge) 100%);
    color: var(--ink);
  }
  .back-cover  { left: 18px;  top: 18px;  width: 384px; height: 560px; }
  .front-cover { left: 440px; top: 18px;  width: 385px; height: 557px; }
  .extras      { left: 18px;  top: 648px; width: 384px; height: 552px; }
  .trial       { left: 440px; top: 648px; width: 385px; height: 552px; }

  .photo {
    position: absolute;
    border: 3px solid var(--photo-border);
    box-shadow: 0 2px 6px rgba(0,0,0,.35);
  }

  /* Back cover */
  .contact { position: absolute; left: 0; width: 100%; text-align: center; color: var(--cream);
    font-family: "Della Respira", serif; text-shadow: 0 1px 2px rgba(0,0,0,.4); white-space: nowrap; }
  .contact__title { top: 160px; font-size: 19px; }
  .contact__phone { top: 188px; font-size: 26px; }
  .contact__label { top: 248px; font-size: 16px; }
  .contact__address { top: 272px; font-size: 15.5px; line-height: 24px; }
  .contact__web { top: 394px; font-family: "Kalam", cursive; font-size: 17px; }

  /* Front cover */
  .brand { position: absolute; left: 108px; top: 228px; width: 270px; text-align: center; color: var(--cream);
    font-family: "Sorts Mill Goudy", serif; font-size: 72px; line-height: 64px; font-weight: 400;
    text-shadow: 0 2px 4px rgba(0,0,0,.35); white-space: nowrap; }
  .tagline { position: absolute; left: 100px; top: 404px; width: 290px; text-align: center; color: var(--cream);
    font-family: "Kalam", cursive; font-weight: 700; font-size: 16px; line-height: 19px; white-space: nowrap; }
  .front-phone { position: absolute; left: 158px; top: 470px; color: var(--cream);
    font-family: "Della Respira", serif; font-size: 30px; white-space: nowrap; }
  .front-web { position: absolute; left: 192px; top: 508px; color: var(--cream);
    font-family: "Kalam", cursive; font-size: 14px; white-space: nowrap; }
  .burst { position: absolute; left: 10px; top: 442px; width: 130px; height: 116px; }

  /* Extras */
  .extras__heading { position: absolute; left: 150px; top: 18px; width: 230px; text-align: center;
    font-family: "Della Respira", serif; font-size: 27px; line-height: 34px; font-weight: 400; }
  .extras__list { position: absolute; left: 172px; top: 110px; width: 210px; list-style: none;
    font-family: "Della Respira", serif; font-size: 12.5px; line-height: 16px; }
  .extras__list li { position: relative; margin-bottom: 7px; padding-left: 2px; white-space: nowrap; }
  .extras__list li::before { content: "•"; position: absolute; left: -18px; }
  .extras__list .sub { display: block; padding-left: 14px; }
  .extras__rule { position: absolute; left: 160px; top: 474px; width: 220px; border-top: 1px solid #9c9178; }
  .extras__note { position: absolute; left: 160px; top: 484px; width: 220px; text-align: center;
    font-family: "Della Respira", serif; font-size: 15px; line-height: 22px; white-space: nowrap; }

  /* Trial */
  .trial__free { position: absolute; left: 6px; top: 2px; font-family: "Sorts Mill Goudy", serif;
    color: var(--red); font-size: 52px; line-height: 56px; white-space: nowrap; }
  .trial__title { position: absolute; left: 150px; top: 12px; width: 228px; font-family: "Sorts Mill Goudy", serif;
    font-size: 34px; line-height: 38px; font-weight: 400; white-space: nowrap; }
  .trial__small { position: absolute; left: 170px; top: 50px; width: 205px; text-align: right;
    font-family: "Della Respira", serif; font-size: 5.5px; white-space: nowrap; }
  .trial__rule { position: absolute; left: 0; width: 100%; border-top: 1.5px solid var(--green-rule); }
  .trial__easy { position: absolute; left: 158px; top: 80px; font-family: "Kalam", cursive; font-weight: 700; font-size: 19px; white-space: nowrap; }
  .trial__easy em { font-style: normal; color: var(--red); }
  .steps { position: absolute; left: 178px; top: 116px; font-family: "Della Respira", serif; font-size: 11.5px; line-height: 22px; white-space: nowrap; }
  .steps li { padding-left: 4px; }
  .prices { position: absolute; left: 0; top: 292px; width: 100%; text-align: center;
    font-family: "Della Respira", serif; font-size: 17px; line-height: 26px; white-space: nowrap; }
  .quote { position: absolute; left: 8px; top: 368px; width: 238px; font-family: "Della Respira", serif;
    font-size: 8.5px; line-height: 13.5px; }
  .quote cite { display: block; text-align: right; font-style: normal; margin-top: 4px; }
  .trial__footer { position: absolute; left: 0; top: 504px; width: 100%; text-align: center;
    font-family: "Della Respira", serif; font-size: 11px; line-height: 16px; white-space: nowrap; }
  .trial__footer small { display: block; font-size: 8px; margin-top: 2px; }
</style>
</head>
<body>
<main class="canvas">

  <section class="panel panel--wood back-cover">
    <div class="photo" role="img" aria-label="Photo of aubergine, lettuce and peppers" style="left:14px;top:18px;width:118px;height:90px;transform:rotate(-3deg);background:linear-gradient(135deg,#2b2435,#6b9a3a 60%,#c9a23b);"></div>
    <div class="photo" role="img" aria-label="Photo of radicchio and corn cobs" style="left:134px;top:14px;width:118px;height:98px;transform:rotate(2deg);background:linear-gradient(135deg,#8a2d4a,#e3c247 60%,#7a9a35);"></div>
    <div class="photo" role="img" aria-label="Photo of green beans, peas and peppers" style="left:250px;top:20px;width:124px;height:92px;transform:rotate(-2deg);background:linear-gradient(135deg,#3f7a2a,#6cae3a 60%,#e09a2c);"></div>

    <p class="contact contact__title">How to contact Dorans Greens</p>
    <p class="contact contact__phone">0800 555 0142</p>
    <p class="contact contact__label">Postal address:</p>
    <p class="contact contact__address">Dorans Greens Limited<br>Unit 5 Riverside Yard • Mill Lane<br>Ashbury • Wessex • AB1 2CD</p>
    <p class="contact contact__web">www.doransgreens.co.uk</p>

    <div class="photo" role="img" aria-label="Photo of salad leaves, tomatoes and artichoke" style="left:14px;top:440px;width:118px;height:104px;transform:rotate(-3deg);background:linear-gradient(135deg,#5c9a2e,#d06a2a 55%,#6e8a4a);"></div>
    <div class="photo" role="img" aria-label="Photo of red peppers and cabbage" style="left:134px;top:448px;width:116px;height:100px;transform:rotate(2deg);background:linear-gradient(135deg,#5a3c5c,#c8261e 55%,#3a4a5a);"></div>
    <div class="photo" role="img" aria-label="Photo of garlic bulbs" style="left:252px;top:440px;width:118px;height:100px;transform:rotate(-3deg);background:linear-gradient(135deg,#e6d4cf,#b88a9a 55%,#9a3030);"></div>
  </section>

  <section class="panel panel--wood front-cover">
    <div role="img" aria-label="Photo of fresh vegetables framing the cover: potatoes, tomatoes, cucumbers, chillies, onions and garlic" style="position:absolute;inset:0;background:
      radial-gradient(ellipse 230px 130px at 55% 8%, rgba(190,140,80,.95), rgba(190,140,80,0) 100%),
      radial-gradient(ellipse 90px 200px at 10% 45%, rgba(60,120,40,.9), rgba(60,120,40,0) 100%),
      radial-gradient(ellipse 80px 120px at 5% 20%, rgba(200,40,30,.85), rgba(200,40,30,0) 100%),
      radial-gradient(ellipse 70px 60px at 92% 14%, rgba(80,150,50,.85), rgba(80,150,50,0) 100%),
      radial-gradient(ellipse 60px 50px at 88% 30%, rgba(170,110,170,.8), rgba(170,110,170,0) 100%),
      radial-gradient(ellipse 60px 120px at 6% 80%, rgba(220,110,30,.85), rgba(220,110,30,0) 100%);"></div>

    <h1 class="brand">Dorans<br>Greens</h1>
    <p class="tagline">Farm Fresh Fruit and Vegetables<br>direct to your doorstep!</p>

    <svg class="burst" viewBox="0 0 130 116" aria-label="Free trial box offer">
      <polygon fill="var(--burst)" points="65,2 74,18 90,6 93,24 112,18 106,36 126,40 112,54 128,66 110,74 120,92 100,92 102,112 84,104 76,116 64,102 52,116 44,102 26,110 26,92 6,92 16,74 0,64 16,54 4,40 24,36 18,18 38,24 42,6 56,18"/>
      <text x="65" y="52" text-anchor="middle" font-family="Kalam, cursive" font-weight="700" font-size="16" fill="var(--burst-ink)" transform="rotate(-10 65 58)">Free Trial</text>
      <text x="65" y="70" text-anchor="middle" font-family="Kalam, cursive" font-weight="700" font-size="13" fill="var(--burst-ink)" transform="rotate(-10 65 58)">Box Offer!</text>
      <text x="65" y="86" text-anchor="middle" font-family="Kalam, cursive" font-size="8" fill="var(--burst-ink)" transform="rotate(-10 65 58)">see inside for details</text>
    </svg>

    <p class="front-phone">0800 555 0142</p>
    <p class="front-web">www.doransgreens.co.uk</p>
  </section>

  <section class="panel panel--parchment extras">
    <div class="photo" role="img" aria-label="Photo of sliced steak" style="left:12px;top:10px;width:124px;height:100px;transform:rotate(-3deg);background:linear-gradient(135deg,#5a2a1e,#b0453a 55%,#d8c6b0);"></div>
    <div class="photo" role="img" aria-label="Photo of artisan bread loaf" style="left:12px;top:116px;width:126px;height:104px;transform:rotate(2deg);background:linear-gradient(135deg,#3a2a1e,#8a5a36 55%,#c89a6a);"></div>
    <div class="photo" role="img" aria-label="Photo of sausages with mash and greens" style="left:12px;top:228px;width:126px;height:104px;transform:rotate(-2deg);background:linear-gradient(135deg,#eee8de,#8a4a2a 50%,#4a7a2a);"></div>
    <div class="photo" role="img" aria-label="Photo of savoury crumble" style="left:12px;top:336px;width:126px;height:100px;transform:rotate(2deg);background:linear-gradient(135deg,#4a5a2a,#d8a040 55%,#8a6a30);"></div>
    <div class="photo" role="img" aria-label="Photo of chocolate dessert" style="left:12px;top:442px;width:126px;height:104px;transform:rotate(-2deg);background:linear-gradient(180deg,#e8e2d6,#a0622a 40%,#3a1e14);"></div>

    <h2 class="extras__heading">We don't just do fruit and veg...</h2>
    <ul class="extras__list">
      <li>Amazing meat boxes <span class="sub">(beef, chicken, pork, lamb...)</span></li>
      <li>Award Winning <span class="sub">Gourmet Sausages</span></li>
      <li>Yummy Desserts</li>
      <li>Large Free Range Eggs</li>
      <li>Milk</li>
      <li>Delicious Tray Bakes <span class="sub">made Fresh</span></li>
      <li>Artisan Bread <span class="sub">Made by Hand Not Machine</span></li>
      <li>Rustic Baguettes <span class="sub">with no Preservatives</span><span class="sub">or Additives</span></li>
      <li>Morning Pasties for You to <span class="sub">Wake Up To</span></li>
      <li>Appetizing Savory Crumbles <span class="sub">not forgetting Sweet ones too...</span></li>
    </ul>
    <div class="extras__rule"></div>
    <p class="extras__note">Boxes are delivered on<br>the doorstep before 5am<br>for convenience!</p>
  </section>

  <section class="panel panel--parchment trial">
    <p class="trial__free">FREE</p>
    <h2 class="trial__title">TRIAL OFFER</h2>
    <p class="trial__small">Offer applies to our small box only. A £2 delivery charge applies.</p>
    <div class="trial__rule" style="top:60px;"></div>

    <div class="photo" role="img" aria-label="Photo of a vegetable box with herbs, potatoes and red onion" style="left:8px;top:76px;width:140px;height:196px;transform:rotate(-2deg);background:linear-gradient(160deg,#3a7a2a,#d8b040 40%,#eeeae0 65%,#7a2a5a);"></div>

    <p class="trial__easy">It's <em>easy</em> to get started!</p>
    <ol class="steps">
      <li>Select your box size</li>
      <li>Select your box type</li>
      <li>Fill your box with Fruit and Vegetables</li>
      <li>Add Fresh Free Range Eggs</li>
      <li>Add Monthly Potatoes</li>
      <li>Add pantry and other products</li>
      <li>Tell us where to deliver!</li>
    </ol>

    <div class="trial__rule" style="top:286px;"></div>
    <p class="prices">Large box for £18.50 • Medium box for £13.00<br>Small box for £7.50</p>
    <div class="trial__rule" style="top:356px;"></div>

    <blockquote class="quote">
      "I just wanted to say that I received my first box last week and I was absolutely delighted with the quality and the freshness of the fruit and veg included. All of the family have actually been enjoying the veg including my toddler who usually will not eat shop brought vegetables. Your produce tastes exactly as it should, lovely and fresh! Thanks..."
      <cite>~ Hannah</cite>
    </blockquote>
    <div class="photo" role="img" aria-label="Photo of mixed vegetables: artichokes, peppers, onions and leeks" style="left:258px;top:352px;width:116px;height:142px;transform:rotate(2deg);background:linear-gradient(150deg,#4a6a3a,#c83a2a 35%,#e8a030 60%,#6a9a3a);"></div>

    <div class="trial__rule" style="top:494px;"></div>
    <p class="trial__footer">You may upgrade to a larger box after your trial simply<br>by logging into your Dorans Greens account.<small>We will make a £2.00 charge for delivery.</small></p>
  </section>

</main>
</body>
</html>
```